ガソリンスタンド店頭での自動車保険の販売を考えています。
保険商品は情報の非対称性が高く、ほとんどの顧客が自身の補償内容をよく把握しいません。また販売方の十分な説明ができていないケースも多いです。そこでよくある補償のミスマッチの例を挙げて保険の見直しを促していきたいと考えています。具体的なミスマッチは以下の三点です。

①車両保険について
車両保険のは一般と限定の二種類がありますが限定では自損事故や当て逃げの際の費用は補償されません。これを理解していない顧客は多いです。

②弁護士費用
任意保険に未加入の自動車ユーザーは地域によってだいぶ変わりますが全体の4割程度います。任意保険未加入の自動車と事故を起こした場合相手に過失がある場合でも物損であれば泣き寝入りするしかありません。また人身事故の場合でも自賠責の補償範囲を超す部分については自腹で清算する必要があります。弁護士を立て相手方と交渉することはできますが莫大な費用がかかります。
弁護士費用特約に加入していればこうした状況を回避することができます。費用的にも数百円程度の付加保険料で済みます。

③運転者限定
実際に運転をする方を限定することで、また年齢条件を設定することにより保険料の減額が見込めます。
しかし保険の組み方が複雑なため補償が受けられない、また過剰な補償となっている場合が数多くあります。

保険は敬遠されがちな分野ですので固くなりすぎず、親しみやすい雰囲気のPOPにしてもらえたらと思います。またPOPの種類や形状等も同時に提案してもらえれば助かります。「加入するかはどうか置いといて無駄や不足があるといけませんので一度補償内容の見直しをされませんか?」というスタイルで販売活動を進めていきますのでそれに沿ったPOPを作って欲しいと思います。
上記①②③に対応した保険会社のパンフレットを添付します。参考にしてください。
補足です。
当社調べでは他社契約分について、適正な補償内容になっていない方は8割程度いらっしゃいました。見た方が自分は大丈夫だろうかと注意喚起出来るような内容にして欲しいと思います。
自体や雰囲気ですが全体的に堅い印象のデザインが多かったのでもう少しポップな感じ、親しみやすい感じにしてほしいです。
すいません、延期させて頂きます。
延長します。
延期します…

やわらかいタッチで、誰が見てもわかりやすい内容でした。

ありがとうございました。

来年より、活用させていただきます。

ご提案いただきありがとうございました。

```html
<!DOCTYPE html>
<html lang="ja">
<head>
<meta charset="utf-8">
<title>その保険 足りてない? ムダじゃない?</title>
<link href="https://fonts.googleapis.com/css2?family=M+PLUS+Rounded+1c:wght@500;700;800&display=swap" rel="stylesheet">
<style>
  :root {
    --sky: #8fcdf0;
    --sky-light: #d6eefb;
    --navy: #1d5f9e;
    --ink: #1f2a3a;
    --red: #e5231b;
    --white: #ffffff;
    --car-green: #5eae3c;
    --car-orange: #f08a1c;
    --scene-warm: #f6c99a;
    --scene-gray: #b9c6d0;
  }
  * { box-sizing: border-box; margin: 0; padding: 0; }
  html, body { width: 846px; height: 1200px; overflow: hidden; }
  body {
    font-family: "M PLUS Rounded 1c", sans-serif;
    background: var(--sky);
    color: var(--ink);
    position: relative;
  }
  .headline {
    position: absolute; top: 40px; left: 0; width: 100%;
    text-align: center; color: var(--white);
    font-size: 168px; font-weight: 800; letter-spacing: 8px; line-height: 1;
  }
  .bubble {
    position: absolute; top: 250px;
    background: var(--white); border: 4px solid var(--ink); border-radius: 40px;
    font-size: 36px; font-weight: 800; padding: 10px 34px; line-height: 1.2;
  }
  .bubble::after {
    content: ""; position: absolute; bottom: -18px; left: 50%; margin-left: -14px;
    width: 24px; height: 24px; background: var(--white);
    border-right: 4px solid var(--ink); border-bottom: 4px solid var(--ink);
    transform: rotate(45deg);
  }
  .bubble--short { left: 120px; }
  .bubble--waste { right: 90px; }
  .car {
    position: absolute; top: 335px; width: 300px; height: 210px; border-radius: 60px 60px 24px 24px;
  }
  .car--green { left: 70px; background: linear-gradient(180deg, #7cc65a, var(--car-green)); }
  .car--orange { right: 70px; background: linear-gradient(180deg, #f6a44a, var(--car-orange)); }
  .versus {
    position: absolute; top: 390px; left: 363px; width: 120px; height: 120px;
    border-radius: 50%; background: var(--navy); color: var(--white);
    font-size: 54px; font-weight: 800; display: flex; align-items: center; justify-content: center;
    border: 5px solid var(--white);
  }
  .checkpoint-band {
    position: absolute; top: 578px; left: 0; width: 100%; height: 54px;
    background: var(--navy); color: var(--white);
    font-size: 28px; font-weight: 700; text-align: center; line-height: 54px;
  }
  .points {
    position: absolute; top: 640px; left: 36px; width: 774px; height: 505px;
    display: flex; gap: 14px;
  }
  .point {
    flex: 1; background: var(--sky-light); border-radius: 6px;
    padding: 8px 12px 12px; display: flex; flex-direction: column;
  }
  .point-head { display: flex; align-items: flex-end; gap: 6px; height: 56px; }
  .point-num { color: var(--red); font-size: 62px; font-weight: 800; line-height: 0.9; font-style: normal; }
  .point-title { font-size: 30px; font-weight: 800; line-height: 1; padding-bottom: 4px; }
  .point-quote {
    margin-top: 8px; background: var(--white); border: 3px solid var(--ink); border-radius: 10px;
    font-size: 19px; font-weight: 700; line-height: 1.35; padding: 8px 10px; min-height: 84px;
  }
  .point-ask { margin-top: 8px; color: var(--navy); font-size: 15px; font-weight: 700; }
  .point-body { margin-top: 6px; font-size: 14px; font-weight: 500; line-height: 1.55; }
  .point-body em { color: var(--red); font-style: normal; font-weight: 700; }
  .point-scene { margin-top: auto; height: 170px; border-radius: 6px; }
  .scene--fire { background: linear-gradient(180deg, var(--scene-warm), #e9804a); }
  .scene--crash { background: linear-gradient(180deg, var(--scene-gray), #9cc98a); }
  .scene--family { background: linear-gradient(180deg, #fbe3cf, var(--scene-warm)); }
  .footer-band {
    position: absolute; bottom: 0; left: 0; width: 100%; height: 50px;
    background: var(--navy); color: var(--white);
    font-size: 24px; font-weight: 700; text-align: center; line-height: 50px;
  }
</style>
</head>
<body>
  <h1 class="headline">その保険</h1>

  <div class="bubble bubble--short">足りてない?</div>
  <div class="bubble bubble--waste">ムダじゃない?</div>

  <div class="car car--green" role="img" aria-label="正面を向いた緑色の車のイラスト"></div>
  <div class="car car--orange" role="img" aria-label="正面を向いたオレンジ色の車のイラスト"></div>
  <div class="versus">Vs.</div>

  <div class="checkpoint-band">保険を見直すなら、チェックポイントはこの3つ</div>

  <section class="points">
    <article class="point">
      <div class="point-head"><b class="point-num">1</b><h2 class="point-title">車両保険</h2></div>
      <p class="point-quote">単独事故なんて起こさないから大丈夫</p>
      <p class="point-ask">なんて思っていませんか?</p>
      <p class="point-body"><em>運転や火災・台風</em>など避けられない損害にも車両保険は役立ちます。ただし限定タイプでは<em>単独事故や当て逃げ</em>は補償されないので注意が必要です。</p>
      <div class="point-scene scene--fire" role="img" aria-label="燃えている車のイラスト"></div>
    </article>
    <article class="point">
      <div class="point-head"><b class="point-num">2</b><h2 class="point-title">弁護士費用</h2></div>
      <p class="point-quote">自分に過失が無ければ弁償してもらえる</p>
      <p class="point-ask">そんな場合ばかりじゃないかも?</p>
      <p class="point-body">100%相手が悪くても、相手が任意保険未加入だと払ってくれない事もあります。こんな時、<em>弁護士に依頼する費用を保険でカバー</em>できます。</p>
      <div class="point-scene scene--crash" role="img" aria-label="車同士の接触事故のイラスト"></div>
    </article>
    <article class="point">
      <div class="point-head"><b class="point-num">3</b><h2 class="point-title">運転者限定</h2></div>
      <p class="point-quote">この車は息子には運転させない</p>
      <p class="point-ask">それなら保険料が安くなるかも?</p>
      <p class="point-body">運転する人が決まっていれば運転者を限定することで保険料を抑えることが可能。<em>運転者限定や運転者年齢条件</em>を見直しましょう。</p>
      <div class="point-scene scene--family" role="img" aria-label="家族のイラスト"></div>
    </article>
  </section>

  <footer class="footer-band">詳しくはスタッフまで! お気軽にご質問ください。</footer>
</body>
</html>
```